Energy trading company (Voltrisa) needs a business card

We need a business card for a company based in Central America. Our main purpose is trading energy . We already have the logo but we need some good creativity to design a high impact business card. Colors blue, orange, green can be used or we would like to see good combinatios with our logo

Target Market(s)

Energy

Industry/Entity Type

Power Generation

Contact Information for Business Card

Logo , headquarters , name, background

Font styles to use
Serif
Sans Serif

Colors

Designer to choose colors to be used in the design.

Requirements
Must have
• it must have a fresh and clean view
Nice to have
• good backgrounds that combine with the logo
Should not have
• too much words

```html
<!DOCTYPE html>
<html lang="en">
<head>
<meta charset="UTF-8">
<title>Voltrisa Business Card</title>
<link rel="stylesheet" href="https://fonts.googleapis.com/css2?family=Montserrat:wght@400;500;700&display=swap">
<style>
  :root {
    --brand-orange: #f7931e;
    --brand-orange-deep: #e57f10;
    --paper-white: #ffffff;
    --backdrop: #4b4b4b;
    --card-shadow: rgba(0, 0, 0, 0.35);
  }
  * { margin: 0; padding: 0; box-sizing: border-box; }
  html, body {
    width: 1200px;
    height: 1125px;
    overflow: hidden;
    background: var(--backdrop);
    font-family: "Montserrat", sans-serif;
  }
  .card {
    position: absolute;
    left: 160px;
    width: 880px;
    height: 503px;
    box-shadow: 0 10px 24px var(--card-shadow);
    overflow: hidden;
  }
  /* Back side */
  .card--back {
    top: 40px;
    background: var(--brand-orange);
  }
  .card--back .back-disc {
    position: absolute;
    left: 70px;
    top: 50%;
    width: 380px;
    height: 380px;
    margin-top: -190px;
    border-radius: 50%;
    background: linear-gradient(90deg, var(--brand-orange-deep), #f9a64a);
    opacity: 0.55;
  }
  .card--back .back-wordmark {
    position: absolute;
    right: 60px;
    top: 50%;
    transform: translateY(-50%);
    color: var(--paper-white);
    font-weight: 500;
    font-size: 62px;
    letter-spacing: 2px;
  }
  /* Front side */
  .card--front {
    top: 582px;
    background: var(--paper-white);
  }
  .front-wordmark {
    position: absolute;
    left: 58px;
    top: 52px;
    color: var(--brand-orange);
    font-weight: 500;
    font-size: 54px;
    letter-spacing: 1px;
  }
  .front-disc {
    position: absolute;
    right: -20px;
    top: 60px;
    width: 440px;
    height: 440px;
    border-radius: 50%;
    background: var(--brand-orange);
  }
  .person {
    position: absolute;
    left: 58px;
    top: 168px;
    color: var(--brand-orange);
  }
  .person-name {
    font-weight: 700;
    font-size: 26px;
    letter-spacing: 0.5px;
  }
  .person-role {
    font-size: 20px;
    margin-top: 2px;
  }
  .address {
    position: absolute;
    left: 58px;
    top: 258px;
    color: var(--brand-orange);
    font-size: 21px;
    line-height: 1.35;
  }
  .contact-list {
    position: absolute;
    left: 58px;
    top: 358px;
    list-style: none;
    color: var(--brand-orange);
    font-size: 22px;
    line-height: 1.5;
  }
  .contact-list li {
    display: flex;
    align-items: center;
    gap: 16px;
  }
  .contact-icon {
    width: 20px;
    height: 20px;
    fill: var(--brand-orange);
    flex: none;
  }
</style>
</head>
<body>

<section class="card card--back" aria-label="Card back">
  <div class="back-disc"></div>
  <div class="back-wordmark">VOLTRISA</div>
</section>

<section class="card card--front" aria-label="Card front">
  <div class="front-wordmark">VOLTRISA</div>

  <div class="person">
    <div class="person-name">DARIO VELMONT</div>
    <div class="person-role">Manager</div>
  </div>

  <div class="address">
    Your address<br>
    city, state, ZIP 0000
  </div>

  <ul class="contact-list">
    <li>
      <svg class="contact-icon" viewBox="0 0 24 24" aria-hidden="true">
        <path d="M6.6 10.8c1.4 2.8 3.8 5.1 6.6 6.6l2.2-2.2c.3-.3.7-.4 1-.2 1.1.4 2.3.6 3.6.6.6 0 1 .4 1 1V20c0 .6-.4 1-1 1C10.6 21 3 13.4 3 4c0-.6.4-1 1-1h3.5c.6 0 1 .4 1 1 0 1.3.2 2.5.6 3.6.1.3 0 .7-.2 1L6.6 10.8z"/>
      </svg>
      123-456-2100
    </li>
    <li>
      <svg class="contact-icon" viewBox="0 0 24 24" aria-hidden="true">
        <path d="M2 5h20v14H2z M3 6.5v.3l9 6 9-6v-.3z" fill-rule="evenodd"/>
      </svg>
      youremail@mailbox.com
    </li>
    <li>
      <svg class="contact-icon" viewBox="0 0 24 24" aria-hidden="true">
        <circle cx="12" cy="12" r="10"/>
        <path d="M2 12h20M12 2c3 3 3 17 0 20M12 2c-3 3-3 17 0 20" stroke="#fff" stroke-width="1.6" fill="none"/>
      </svg>
      www.yourwebsite.com
    </li>
  </ul>

  <div class="front-disc"></div>
</section>

</body>
</html>
```